Premium Gold Vodka Label Design

English ------------------- We need a label for a Vodka Bottle. Its a sparkling premium vodka with gold inside. The design should look premium. We tried it on our selves but it looks horrible. Therefore we need your help. The current name is corvelle K, but we are open for any better suggestion. We attached the selfmade design. The label will be printed on the bottle. We have other design jobs for you (logo, other sorts)! English ------------------------ We need a label for a vodka bottle. This is a premium vodka which is offset with gold. The design should look like this. We have tried so far and failed. That is why we need your support. The name is so far corvelle K. If you have better suggestions we would be pleased about other suggestions / ideas. In the appendix the failed design is stored. The label is to be applied by screen printing. In the case of good work follow-up projects are guaranteed (logo, other varieties, etc)!
Updates

Reason: We need more time for the decision.

Target Market(s)

USA

Colors

Designer to choose colors to be used in the design.

Requirements
Must have
• English ------------------------ The needed text is on our selfmade label that is attached. English ------------------------ The required texts are stored in the attached design.
Nice to have
• English ------------------------ Transparent places are allowed because we want to print the label on the bottom. English ------------------------ As the label is applied by screen printing, transparent areas are also possible.

```html
<!DOCTYPE html>
<html lang="en">
<head>
<meta charset="utf-8">
<title>Corvelle K 24 KT Vodka Label</title>
<link href="https://fonts.googleapis.com/css2?family=Oswald:wght@200;300;400;600&display=swap" rel="stylesheet">
<style>
  :root {
    --label-black: #000000;
    --gold-light: #f6e27c;
    --gold: #d9b21f;
    --gold-deep: #b98a12;
    --copper: #c8601a;
  }
  html, body {
    margin: 0;
    padding: 0;
    overflow: hidden;
    background: var(--label-black);
  }
  .label {
    position: relative;
    width: 694px;
    height: 1200px;
    background: var(--label-black);
    overflow: hidden;
    font-family: "Oswald", sans-serif;
    text-align: center;
  }
  .side-rules {
    position: absolute;
    inset: 0;
  }
  .gold-text {
    background: linear-gradient(90deg, var(--gold-deep), var(--gold-light) 45%, var(--gold) 70%, var(--gold-deep));
    -webkit-background-clip: text;
    background-clip: text;
    color: transparent;
  }
  .line {
    position: absolute;
    left: 0;
    right: 0;
    margin: 0;
    line-height: 1;
    text-transform: uppercase;
  }
  .brand-mark {
    top: 92px;
    font-size: 28px;
    font-weight: 400;
    letter-spacing: 4px;
    color: var(--gold);
  }
  .brand-name {
    top: 200px;
    font-size: 74px;
    font-weight: 600;
    letter-spacing: 1px;
  }
  .karat {
    top: 325px;
    font-size: 74px;
    font-weight: 600;
  }
  .tagline {
    top: 474px;
    font-size: 33px;
    font-weight: 300;
    word-spacing: 4px;
  }
  .product {
    top: 718px;
    font-size: 150px;
    font-weight: 200;
    letter-spacing: 6px;
  }
  .process {
    top: 918px;
    font-size: 40px;
    font-weight: 300;
  }
  .process strong { font-weight: 600; }
  .origin {
    top: 978px;
    font-size: 40px;
    font-weight: 300;
  }
  .specs {
    top: 1130px;
    font-size: 22px;
    font-weight: 400;
    display: flex;
    justify-content: center;
    gap: 22px;
  }
  .specs .divider {
    display: inline-block;
    width: 2px;
    height: 28px;
    margin-top: -3px;
    background: var(--gold);
  }
</style>
</head>
<body>
<main class="label">
  <svg class="side-rules" width="694" height="1200" viewBox="0 0 694 1200" aria-hidden="true">
    <defs>
      <linearGradient id="rule-gold" x1="0" y1="0" x2="0" y2="1">
        <stop offset="0" stop-color="#e9c84a"/>
        <stop offset="0.55" stop-color="#d9a020"/>
        <stop offset="1" stop-color="#c8601a"/>
      </linearGradient>
    </defs>
    <g stroke="url(#rule-gold)" stroke-width="2.2">
      <line x1="72" y1="0" x2="72" y2="1200"/>
      <line x1="90" y1="0" x2="90" y2="1200"/>
      <line x1="108" y1="0" x2="108" y2="1200"/>
      <line x1="128" y1="0" x2="128" y2="1200"/>
      <line x1="565" y1="0" x2="565" y2="1200"/>
      <line x1="585" y1="0" x2="585" y2="1200"/>
      <line x1="604" y1="0" x2="604" y2="1200"/>
      <line x1="622" y1="0" x2="622" y2="1200"/>
    </g>
  </svg>

  <p class="line brand-mark">Corvelle K</p>
  <h1 class="line brand-name gold-text">Corvelle K</h1>
  <p class="line karat gold-text">24 KT</p>
  <p class="line tagline gold-text">Premium Gold Sparkling</p>
  <h2 class="line product gold-text">Vodka</h2>
  <p class="line process gold-text">Distilled <strong>8</strong> Filtered</p>
  <p class="line origin gold-text">Made in Germany</p>
  <p class="line specs">
    <span class="gold-text">40% Alc Vol</span>
    <span class="divider"></span>
    <span class="gold-text">200 ml</span>
    <span class="divider"></span>
    <span class="gold-text">80 Proof</span>
  </p>
</main>
</body>
</html>
```